Verostel business card

Business card for sustainable investment company called "Verostel". Verostel is an exchange platform selling carbon credits between buyers and sellers. Carbon Credits are an environmental commodity for reducing global carbon emissions.

the card should obviously have our logo and the theme should be sustainability/environment mixed with a trading platform.

Contact Information for Business Card

Logo, Name, Title, Phone, Email

Colors
0054AA
0677BA
7BADD7
CADEEF
E8F1F8
0094D4
00A9DD
6FCCEA
C7EBF8
E9F6FB
00AB8E
00BBA5
67D7C9
C6EFE9
E9F9F6
59FF00
82FF00
B8FF75
E3FFCB
F4FFEA

```html
<!DOCTYPE html>
<html lang="en">
<head>
<meta charset="utf-8">
<title>Verostel business card</title>
<link rel="stylesheet" href="https://fonts.googleapis.com/css2?family=Montserrat:wght@700&family=Open+Sans:wght@400;600;700&display=swap">
<style>
  :root {
    --page: #e6ebf1;
    --navy: #142a52;
    --white: #ffffff;
    --sky: #5cc3dc;
    --blue: #4f86cc;
    --mark: #5aa6da;
    --rule: rgba(255, 255, 255, 0.85);
  }
  * { margin: 0; padding: 0; box-sizing: border-box; }
  html, body { width: 1200px; height: 780px; overflow: hidden; }
  body {
    background: var(--page);
    font-family: "Open Sans", Arial, sans-serif;
    position: relative;
  }
  .card {
    position: absolute;
    top: 235px;
    width: 520px;
    height: 310px;
    border-radius: 18px;
    background: var(--navy);
    overflow: hidden;
    box-shadow: 0 10px 24px rgba(20, 42, 82, 0.25);
    color: var(--white);
  }
  .card--front { left: 60px; }
  .card--back { left: 620px; }
  .edge-band {
    position: absolute;
    left: 0; bottom: 0;
    width: 520px; height: 14px;
  }

  /* front */
  .brand-mark {
    position: absolute;
    left: 38px; top: 66px;
    display: flex; align-items: center; gap: 14px;
  }
  .brand-dot {
    width: 76px; height: 76px; border-radius: 50%;
    background: var(--mark);
  }
  .brand-name {
    font-weight: 700; font-size: 26px; color: var(--mark);
    letter-spacing: 0.5px;
  }
  .divider { position: absolute; left: 240px; top: 40px; }
  .person {
    position: absolute; left: 300px; top: 70px;
  }
  .person-name {
    font-weight: 700; font-size: 24px; color: var(--sky); line-height: 1.15;
  }
  .person-title {
    font-weight: 600; font-size: 15px; color: var(--white); margin-top: 2px;
  }
  .contact-list { list-style: none; margin-top: 16px; }
  .contact-item {
    display: flex; align-items: center; gap: 8px;
    font-size: 14px; line-height: 1.65;
  }
  .contact-icon { width: 14px; height: 14px; flex: none; }
  .address {
    position: absolute; left: 38px; bottom: 34px;
    font-size: 13px; letter-spacing: 0.2px;
  }

  /* back */
  .wordmark {
    position: absolute; left: 0; right: 0; top: 0; bottom: 14px;
    display: flex; align-items: center; justify-content: center; gap: 18px;
  }
  .wordmark-dot {
    width: 58px; height: 58px; border-radius: 50%; background: var(--mark);
  }
  .wordmark-name {
    font-family: "Montserrat", Arial, sans-serif;
    font-weight: 700; font-size: 46px; letter-spacing: 2px; color: var(--white);
  }
</style>
</head>
<body>

<section class="card card--front" aria-label="Card front">
  <div class="brand-mark">
    <span class="brand-dot"></span>
    <span class="brand-name">Verostel</span>
  </div>

  <svg class="divider" width="60" height="200" viewBox="0 0 60 200" aria-hidden="true">
    <line x1="58" y1="2" x2="2" y2="198" stroke="var(--rule)" stroke-width="1.2"/>
  </svg>

  <div class="person">
    <h1 class="person-name">Lenka Marovic</h1>
    <p class="person-title">Managing Director</p>
    <ul class="contact-list">
      <li class="contact-item">
        <svg class="contact-icon" viewBox="0 0 16 16" aria-hidden="true"><path d="M3.5 1.5l2.5 0 1 3.5-1.7 1.2a8 8 0 0 0 4.5 4.5L11 9l3.5 1v2.5c0 1-1 2-2 2A11 11 0 0 1 1.5 3.5c0-1 1-2 2-2z" fill="var(--mark)"/></svg>
        (555) 014-2236
      </li>
      <li class="contact-item">
        <svg class="contact-icon" viewBox="0 0 16 16" aria-hidden="true"><rect x="1" y="3" width="14" height="10" rx="1.5" fill="var(--mark)"/><path d="M1.5 4l6.5 5 6.5-5" fill="none" stroke="var(--navy)" stroke-width="1.3"/></svg>
        info@verostel.com
      </li>
      <li class="contact-item">
        <svg class="contact-icon" viewBox="0 0 16 16" aria-hidden="true"><circle cx="8" cy="8" r="7" fill="var(--mark)"/><path d="M1 8h14M8 1c-3 3-3 11 0 14M8 1c3 3 3 11 0 14" fill="none" stroke="var(--navy)" stroke-width="1"/></svg>
        www.verostel.com
      </li>
    </ul>
  </div>

  <p class="address">418 Harlow Ave. Suite 300 Denton, TX 76201</p>

  <svg class="edge-band" viewBox="0 0 520 14" preserveAspectRatio="none" aria-hidden="true">
    <defs>
      <linearGradient id="bandFront" x1="0" x2="1" y1="0" y2="0">
        <stop offset="0" stop-color="var(--sky)"/>
        <stop offset="1" stop-color="var(--blue)"/>
      </linearGradient>
    </defs>
    <polygon points="0,0 200,0 208,14 0,14" fill="url(#bandFront)"/>
    <polygon points="214,0 520,0 520,14 222,14" fill="var(--white)"/>
  </svg>
</section>

<section class="card card--back" aria-label="Card back">
  <div class="wordmark">
    <span class="wordmark-dot"></span>
    <span class="wordmark-name">VEROSTEL</span>
  </div>

  <svg class="edge-band" viewBox="0 0 520 14" preserveAspectRatio="none" aria-hidden="true">
    <defs>
      <linearGradient id="bandBack" x1="0" x2="1" y1="0" y2="0">
        <stop offset="0" stop-color="var(--sky)"/>
        <stop offset="1" stop-color="var(--blue)"/>
      </linearGradient>
    </defs>
    <polygon points="0,0 200,0 208,14 0,14" fill="url(#bandBack)"/>
    <polygon points="214,0 520,0 520,14 222,14" fill="var(--white)"/>
  </svg>
</section>

</body>
</html>
```